Lanternleaf - Fresh Asian Cuisine Menu

We need to redo our menu to include pictures of food items. Our restaurant is vibrant, trendy, upscale Chinese cuisine

Requirements
Must have
• Must fit on 8.5x11 paper. We can remove the About Us section if needed but menu cannot be more than 6 pages total. Must include pictures of menu items

```html
<!DOCTYPE html>
<html lang="en">
<head>
<meta charset="utf-8">
<title>Lanternleaf - Fresh Asian Cuisine Menu</title>
<link rel="stylesheet" href="https://fonts.googleapis.com/css2?family=Montserrat:ital,wght@0,300;0,400;0,500;0,600;0,700;1,300&display=swap">
<style>
  :root {
    --backdrop: #e9e4dc;
    --ink-dark: #0b0b0b;
    --paper: #fbfbfb;
    --red: #c4161c;
    --white: #ffffff;
    --muted: #9a9a9a;
    --text-dark: #2a2a2a;
    --rule: #7a7a7a;
  }
  * { box-sizing: border-box; margin: 0; padding: 0; }
  html, body { width: 1200px; height: 800px; overflow: hidden; }
  body {
    background: var(--backdrop);
    font-family: "Montserrat", sans-serif;
  }
  .spread { position: absolute; left: 40px; top: 20px; width: 1120px; height: 760px; display: flex; }
  .page { position: relative; width: 560px; height: 760px; overflow: hidden; }

  /* ---------- menu page ---------- */
  .menu-page { background: var(--ink-dark); color: var(--white); }
  .menu-mark { position: absolute; top: 10px; left: 0; width: 100%; display: flex; align-items: center; justify-content: center; gap: 6px; }
  .menu-mark .dot { width: 14px; height: 14px; border-radius: 50%; background: var(--red); }
  .menu-mark .name { font-size: 13px; font-weight: 600; letter-spacing: 1px; color: var(--white); }

  .section-label { position: absolute; height: 14px; }
  .section-label::before { content: ""; position: absolute; left: 0; right: 0; top: 7px; border-top: 1px solid var(--rule); }
  .section-label span {
    position: absolute; left: 50%; top: 0; transform: translateX(-50%);
    background: var(--white); color: var(--ink-dark);
    font-size: 8px; font-weight: 700; padding: 2px 10px; line-height: 10px; white-space: nowrap;
    clip-path: polygon(6px 0, calc(100% - 6px) 0, 100% 50%, calc(100% - 6px) 100%, 6px 100%, 0 50%);
  }

  .item { position: absolute; width: 235px; }
  .item-name { font-size: 13px; font-weight: 500; line-height: 16px; }
  .item-leader { border-top: 1.5px dotted #bdbdbd; margin: 3px 44px 4px 0; }
  .item-desc { font-size: 8px; font-style: italic; font-weight: 300; color: var(--muted); line-height: 11px; padding-right: 46px; }
  .price {
    position: absolute; right: 0; top: 6px; width: 34px; height: 34px;
    background: var(--white); color: var(--ink-dark);
    font-size: 13px; font-weight: 700; display: flex; align-items: center; justify-content: center;
    clip-path: polygon(30% 0, 70% 0, 100% 30%, 100% 70%, 70% 100%, 30% 100%, 0 70%, 0 30%);
    border-radius: 6px;
  }

  .photo-item { position: absolute; width: 235px; height: 64px; }
  .photo-item .dish-photo {
    position: absolute; left: 0; top: 0; width: 82px; height: 62px;
    background: radial-gradient(circle at 50% 50%, #c65a2c 0 22%, #e9e2d6 24% 40%, #4a3f36 42%);
  }
  .photo-item .item-body { position: absolute; left: 89px; top: 0; right: 0; }
  .photo-item .item-name { font-size: 11px; font-weight: 600; line-height: 12px; }
  .photo-item .price { top: 2px; width: 28px; height: 28px; font-size: 12px; border-radius: 4px; clip-path: none; }
  .photo-item .item-leader { margin: 3px 32px 6px 0; }
  .photo-item .item-desc { padding-right: 0; }

  .column-divider { position: absolute; left: 277px; top: 478px; height: 248px; border-left: 1.5px dotted #bdbdbd; }
  .bottom-rule { position: absolute; left: 35px; right: 35px; top: 740px; border-top: 1px solid var(--rule); }

  /* ---------- story page ---------- */
  .story-page { background: var(--paper); color: var(--text-dark); }
  .brand { position: absolute; top: 30px; left: 0; width: 100%; text-align: center; }
  .brand-line { display: inline-flex; align-items: center; gap: 8px; }
  .brand-line .dot { width: 16px; height: 16px; border-radius: 50%; background: var(--red); }
  .brand-name { font-size: 26px; font-weight: 700; color: var(--ink-dark); letter-spacing: 0.5px; }
  .brand-tagline { font-size: 7px; font-weight: 600; letter-spacing: 1.5px; color: var(--ink-dark); margin-top: 1px; padding-left: 60px; }
  .story-title { position: absolute; top: 92px; left: 0; width: 100%; text-align: center; font-size: 58px; font-weight: 400; color: var(--ink-dark); letter-spacing: 1px; }
  .story-body { position: absolute; top: 192px; left: 45px; width: 450px; font-size: 12px; font-weight: 400; line-height: 15px; color: var(--text-dark); }
  .story-body p { margin-bottom: 15px; }
  .story-emblem { position: absolute; left: 150px; top: 510px; width: 230px; height: 230px; border-radius: 50%; background: var(--red); }
</style>
</head>
<body>
<main class="spread">

  <section class="page menu-page" aria-label="Menu">
    <div class="menu-mark"><span class="dot"></span><span class="name">Lanternleaf</span></div>

    <div class="section-label" style="left:35px; width:485px; top:58px;"><span>NOODLES &amp; RICE</span></div>
    <div class="item" style="left:35px; top:82px;">
      <div class="item-name">Lanternleaf's Fried Rice</div><div class="item-leader"></div>
      <div class="item-desc">Shrimp, chicken, and beef, farm fresh eggs, onions, and scallions</div>
      <div class="price">$12</div>
    </div>
    <div class="item" style="left:285px; top:82px;">
      <div class="item-name">Lanternleaf's Lo Mein</div><div class="item-leader"></div>
      <div class="item-desc">Shrimp, chicken, and beef, farm fresh eggs, onions, and scallions</div>
      <div class="price">$12</div>
    </div>
    <div class="item" style="left:35px; top:138px;">
      <div class="item-name">Vegetarian White Fried Rice</div><div class="item-leader"></div>
      <div class="item-desc">Mixed vegetables with white rice</div>
      <div class="price">$10</div>
    </div>
    <div class="item" style="left:285px; top:138px;">
      <div class="item-name">Lanternleaf's Fried Rice</div><div class="item-leader"></div>
      <div class="item-desc">Mixed vegetables with lo mein noodles</div>
      <div class="price">$10</div>
    </div>

    <div class="section-label" style="left:35px; width:485px; top:200px;"><span>VEGETARIAN DISHES</span></div>
    <div class="item" style="left:35px; top:224px;">
      <div class="item-name">Wok Tossed String Beans</div><div class="item-leader"></div>
      <div class="item-desc">Fresh string beans mixed with pickled vegetables</div>
      <div class="price">$9</div>
    </div>
    <div class="photo-item" style="left:35px; top:278px;">
      <div class="dish-photo" role="img" aria-label="Photo of mapo tofu in a bowl"></div>
      <div class="item-body">
        <div class="item-name">Mapo<br>Tofu</div><div class="item-leader"></div>
        <div class="item-desc">Soft Tofu, scallion, Sichuan pepper-corn and peppers</div>
        <div class="price">$11</div>
      </div>
    </div>
    <div class="photo-item" style="left:35px; top:350px;">
      <div class="dish-photo" role="img" aria-label="Photo of spicy garlic eggplant on a plate"></div>
      <div class="item-body">
        <div class="item-name">Spicy Garlic<br>Eggplant</div><div class="item-leader"></div>
        <div class="item-desc">Shrimp, chicken, and beef, farm fresh eggs, onions, and scallions</div>
        <div class="price">$12</div>
      </div>
    </div>
    <div class="photo-item" style="left:285px; top:227px;">
      <div class="dish-photo" role="img" aria-label="Photo of Buddha's Delight vegetables"></div>
      <div class="item-body">
        <div class="item-name">Buddha's<br>Delight</div><div class="item-leader"></div>
        <div class="item-desc">Seasonal vegetables wok-tossed in our light soy garlic sauce</div>
        <div class="price">$10</div>
      </div>
    </div>
    <div class="photo-item" style="left:285px; top:298px;">
      <div class="dish-photo" role="img" aria-label="Photo of stir-fried eggplant and beans"></div>
      <div class="item-body">
        <div class="item-name">Stir-fried<br>Eggplant Beans</div><div class="item-leader"></div>
        <div class="item-desc">Chinese eggplant with sautéed beansgreen beans</div>
        <div class="price">$10</div>
      </div>
    </div>
    <div class="photo-item" style="left:285px; top:370px;">
      <div class="dish-photo" role="img" aria-label="Photo of shiitake and baby bok choy"></div>
      <div class="item-body">
        <div class="item-name">Shiitake<br>Baby Bok-Choy</div><div class="item-leader"></div>
        <div class="item-desc">Sautéed baby bok-choy with Shiitake mushrooms in brown sauce</div>
        <div class="price">$12</div>
      </div>
    </div>

    <div class="section-label" style="left:35px; width:235px; top:460px;"><span>KIDS MENU</span></div>
    <div class="section-label" style="left:285px; width:235px; top:460px;"><span>DESSERTS</span></div>
    <div class="column-divider"></div>

    <div class="item" style="left:35px; top:484px;">
      <div class="item-name">Beef Lo Mein</div><div class="item-leader"></div>
      <div class="item-desc">Lo Mein noodles mixed with beef in garlic sauce</div>
      <div class="price">$4</div>
    </div>
    <div class="item" style="left:35px; top:530px;">
      <div class="item-name">Chicken Fried Rice</div><div class="item-leader"></div>
      <div class="item-desc">Fried rice, farm fresh eggs, onions, and scallions</div>
      <div class="price">$4</div>
    </div>
    <div class="photo-item" style="left:35px; top:574px;">
      <div class="dish-photo" role="img" aria-label="Photo of sweet and sour chicken"></div>
      <div class="item-body">
        <div class="item-name">Sweet &amp; Sour<br>Chicken</div><div class="item-leader"></div>
        <div class="item-desc">Bite sized crispy chicken with sweet &amp; sour sauce</div>
        <div class="price">$6</div>
      </div>
    </div>
    <div class="photo-item" style="left:35px; top:645px;">
      <div class="dish-photo" role="img" aria-label="Photo of lemon chicken"></div>
      <div class="item-body">
        <div class="item-name">Lemon<br>Chicken</div><div class="item-leader"></div>
        <div class="item-desc">Bite sized crispy chicken in a sweet lemon sauce</div>
        <div class="price">$6</div>
      </div>
    </div>

    <div class="item" style="left:285px; top:484px;">
      <div class="item-name">The Great Wall of Cake</div><div class="item-leader"></div>
      <div class="item-desc">Scale this fortress of Chocolate Cake Delight</div>
      <div class="price">$7</div>
    </div>
    <div class="item" style="left:285px; top:531px;">
      <div class="item-name">Cheesecake Wontons (4)</div><div class="item-leader"></div>
      <div class="item-desc">Fried wontons stuffed with cheesecake and dipped in raspberry sauce</div>
      <div class="price">$6</div>
    </div>
    <div class="item" style="left:285px; top:587px;">
      <div class="item-name">Tempura Snowball</div><div class="item-leader"></div>
      <div class="item-desc">Vanilla ice cream fried in tempura batter with powdered sugar and fudge</div>
      <div class="price">$4</div>
    </div>
    <div class="item" style="left:285px; top:643px;">
      <div class="item-name">Sweet Rice Patties<br>in Caramel</div><div class="item-leader"></div>
      <div class="item-desc">Traditional Chinese dessert with sweet rice dipped in a caramel sauce</div>
      <div class="price" style="top:12px;">$7</div>
    </div>

    <div class="bottom-rule"></div>
  </section>

  <section class="page story-page" aria-label="Our Story">
    <header class="brand">
      <div class="brand-line"><span class="dot"></span><span class="brand-name">LANTERNLEAF</span></div>
      <div class="brand-tagline">FRESH ASIAN CUISINE</div>
    </header>
    <h1 class="story-title">OUR STORY</h1>
    <div class="story-body">
      <p>At Lanternleaf, we pride ourselves in serving fresh, authentic Sichuan Chinese cuisine delicately prepared by our expertly trained Chefs.</p>
      <p>Sichuan cuisine originates from southwest China between the Sichuan Basin and Tibetan Plateau. It is known for being both very spicy and flavorful, much like our own southern Louisiana cuisine.</p>
      <p>Our Executive Chef, Wen Liao grew up in the southwestern Chinese province of Sichuan, China where he began his training at fifteen years old under his grandfather's mentorship. Chef Liao became an acclaimed chef in his province, opening several restaurants and traveling throughout China to cater for many of China's elite. His dream was to share his Sichuan style with the world which lead him to the United States. He has worked in restaurants in both Houston and New York and we now welcome him to his new home in Lafayette, Louisiana.</p>
      <p>We are very excited to bring to Lafayette the authenticity of Chinese cuisine and hope you enjoy your experience dining with us.</p>
    </div>
    <div class="story-emblem"></div>
  </section>

</main>
</body>
</html>
```